Window Cleaning Flyer targeting body corporates

Need a flyer for window cleaning targeting body corporate (approx A5 print size). It should be professional and match the logo attached.
We are looking to standout but not be to over the top for a window cleaning/services company.
We want to entice the receptionist or managers to call us because they see no good reason not to.

Industry/Entity Type

Window Cleaning

Font styles to use
Serif

Colors
0555a3
fbed22

Requirements
Must have
• Professional with a few of the photos attached included. Must include logo and the following contact details:
• Ph: 9413 6570
• email: admin@brightpaneworks.com.au
• PO Box 4726
• Marlowe Heights
• 3284
Nice to have
• Colours matching logo/ van print layout. Looking for more of a simplistic professional design.
Should not have
• Cartoon pictures, animated decorations or stock photos.

```html
<!DOCTYPE html>
<html lang="en">
<head>
<meta charset="utf-8">
<title>Brightpane Window Cleaning – Body Corporate Flyer</title>
<link rel="stylesheet" href="https://fonts.googleapis.com/css2?family=Bebas+Neue&family=Quicksand:wght@500;600&family=Oswald:wght@500;600&family=Fira+Sans:wght@700&display=swap">
<style>
  :root {
    --navy: #0b5487;
    --yellow: #fbed22;
    --yellow-dark: #6b6212;
    --white: #ffffff;
    --soft-white: #e6ecf2;
    --frame: #ffffff;
  }
  * { margin: 0; padding: 0; box-sizing: border-box; }
  html, body { width: 846px; height: 1200px; overflow: hidden; background: var(--navy); }
  .flyer { position: relative; width: 846px; height: 1200px; background: var(--navy); color: var(--white); }

  .headline { position: absolute; left: 0; width: 846px; text-align: center; font-family: "Bebas Neue", sans-serif; line-height: 1; }
  .headline-top { top: 30px; font-size: 44px; }
  .headline-top .brand { color: var(--yellow); }
  .headline-main { top: 74px; font-size: 92px; }

  .intro { position: absolute; top: 172px; left: 20px; width: 806px; text-align: center; font-family: "Quicksand", sans-serif; font-weight: 500; font-size: 27px; line-height: 35px; }

  .photo { position: absolute; left: 34px; width: 294px; height: 189px; background: var(--frame); padding: 8px; }
  .photo-fill { width: 100%; height: 100%; }
  .photo-1 { top: 332px; } .photo-1 .photo-fill { background: linear-gradient(135deg, #2d3b4a, #7f9bb5 55%, #c9d6df); }
  .photo-2 { top: 546px; } .photo-2 .photo-fill { background: linear-gradient(90deg, #6c7a5a, #b9c3c5 45%, #2f4a4e); }
  .photo-3 { top: 759px; } .photo-3 .photo-fill { background: linear-gradient(180deg, #9aa0a3, #8d857e 60%, #7a6e66); }

  .ribbons { position: absolute; left: 0; top: 0; width: 846px; height: 1200px; pointer-events: none; }
  .ribbon { fill: var(--yellow); }
  .ribbon-tail { fill: var(--yellow-dark); }

  .specialises-title { position: absolute; top: 330px; left: 368px; font-family: "Oswald", sans-serif; font-weight: 600; font-style: italic; font-size: 26px; color: #1c2a3a; }

  .services { position: absolute; top: 386px; left: 358px; width: 460px; list-style: none; font-family: "Quicksand", sans-serif; font-weight: 500; font-size: 20.5px; line-height: 25px; }
  .services li { position: relative; padding-left: 32px; margin-bottom: 25px; }
  .services li::before { content: "•"; position: absolute; left: 4px; font-size: 14px; }

  .proud { position: absolute; top: 648px; left: 380px; width: 400px; text-align: center; font-family: "Bebas Neue", sans-serif; font-size: 30px; line-height: 40px; color: #1c2a3a; }

  .cta { position: absolute; left: 357px; width: 400px; text-align: center; font-family: "Oswald", sans-serif; font-weight: 500; }
  .cta-line1 { top: 808px; font-size: 23px; }
  .cta-line2 { top: 840px; font-size: 22px; }
  .cta-line2 strong { font-size: 34px; font-weight: 600; }
  .cta-phone { top: 895px; font-size: 42px; font-weight: 600; letter-spacing: 1px; }

  .logo { position: absolute; left: 32px; top: 1030px; font-family: "Bebas Neue", sans-serif; color: var(--yellow); line-height: 1; }
  .logo-name { display: block; font-size: 92px; }
  .logo-tag { display: block; font-size: 40px; margin-top: 4px; }

  .contact { position: absolute; left: 474px; top: 1034px; font-family: "Fira Sans", sans-serif; font-weight: 700; font-size: 18px; line-height: 25.5px; color: var(--soft-white); font-style: normal; }
</style>
</head>
<body>
<main class="flyer">
  <h1>
    <span class="headline headline-top">Let <span class="brand">Brightpane</span> take care of your body</span>
    <span class="headline headline-main">Corporate needs!</span>
  </h1>
  <p class="intro">With over 15 years of experience we will ensure the job is completed to the highest standard everytime..</p>

  <figure class="photo photo-1"><div class="photo-fill" role="img" aria-label="Two team members cleaning a car showroom's glass frontage with extension poles"></div></figure>
  <figure class="photo photo-2"><div class="photo-fill" role="img" aria-label="Team member cleaning tall office windows with a water-fed pole"></div></figure>
  <figure class="photo photo-3"><div class="photo-fill" role="img" aria-label="Team member pressure washing a concrete driveway"></div></figure>

  <svg class="ribbons" viewBox="0 0 846 1200" aria-hidden="true">
    <polygon class="ribbon-tail" points="356,333 390,287 390,323"/>
    <polygon class="ribbon" points="346,366 356,333 640,323 628,362"/>
    <polygon class="ribbon" points="608,362 656,322 656,324 610,396"/>
    <polygon class="ribbon-tail" points="372,636 460,600 460,636"/>
    <polygon class="ribbon" points="357,735 372,636 760,636 748,735"/>
    <polygon class="ribbon" points="722,700 795,636 781,735 722,757"/>
  </svg>

  <h2 class="specialises-title">Brightpane specialises :</h2>
  <ul class="services">
    <li>Window Cleaning</li>
    <li>Gutter Cleaning (using our ladder free gutter vacuum)</li>
    <li>Pressure Washing including moss treatment to prevent mould regrowth on concrete surface</li>
  </ul>

  <p class="proud">Proud to be friendly and courteous<br>to all residents.</p>

  <p class="cta cta-line1">Contact the Brightpane Team for an easy</p>
  <p class="cta cta-line2">and <strong>FREE quote</strong> today !</p>
  <p class="cta cta-phone">94136570</p>

  <div class="logo">
    <span class="logo-name">BRIGHTPANE</span>
    <span class="logo-tag">WINDOW CLEANING</span>
  </div>

  <address class="contact">
    email: admin@brightpaneworks.com.au<br>
    PO Box 4726<br>
    Marlowe Heights<br>
    3284
  </address>
</main>
</body>
</html>
```